Business Card Design

We need a business card design for a Non-Profit Christian Based Organization located in Milford, Pa.
Alder Ridge Helping Harbor
Is a Christ-centered organization dedicated to providing compassion and hope to homeless or near homeless, families and individuals, by meeting their basic and urgent need of food, clothing and shelter.
Updates
the logo is black and white
and must add the color green some where 00400
Industry/Entity Type
Clothing
Contact Information for Business Card
Alder Ridge Helping Harbor
P.O. Box 287
Brookvale, Pa 18990
Phone: (570) 413-CARE(2273)
Toll Free: (855) 413-CARE
email:Info@alderridgehh.org
email:Careline@alderridgehh.org
Our organization already has a logo.
Front of card:
Is a Christ-centered organization dedicated to providing compassion and hope to homeless or near homes, families and individual by meeting their basic and urgent need of food, clothing and shelter.(this is our Mission Statement)
On back of card:
'I was hungry and you gave me something to eat;
"I was thirsty and you gave me something to drink;
"I was a stranger and you invited me in."
Matthew 25:35
Color: Logo is black and white
Background color I would like a bright light green 00ff00(close to that)
I attached a sample of what I created on Quill Press but, I don't like the color green, nor the design (but I just wanted to give you and Idea of the Logo and Alder Ridge (one line) Helping Harbor (second line) in a different font thank you
Delia Rostova
Pr/Board of Directors

```html
<!DOCTYPE html>
<html lang="en">
<head>
<meta charset="UTF-8">
<title>Alder Ridge Helping Harbor – Business Card</title>
<link rel="stylesheet" href="https://fonts.googleapis.com/css2?family=Sorts+Mill+Goudy&display=swap">
<style>
  :root {
    --card-green: #abc94c;
    --card-green-light: #b8d262;
    --card-green-dark: #9fbe40;
    --ink-white: #ffffff;
    --ink-black: #111111;
    --title-shadow: #2d3a10;
    --page: #ffffff;
  }
  * { box-sizing: border-box; margin: 0; padding: 0; }
  html, body {
    width: 883px;
    height: 1200px;
    overflow: hidden;
    background: var(--page);
  }
  body {
    position: relative;
    font-family: "Sorts Mill Goudy", Georgia, serif;
  }
  .card {
    position: absolute;
    width: 726px;
    height: 426px;
    background:
      radial-gradient(ellipse 80% 40% at 55% 72%, var(--card-green-light) 0%, transparent 70%),
      linear-gradient(160deg, var(--card-green) 0%, var(--card-green) 60%, var(--card-green-dark) 100%);
    overflow: hidden;
  }
  .card--front { left: 39px; top: 78px; }
  .card--back  { left: 114px; top: 661px; }

  .brand-mark {
    position: absolute;
    left: 0;
    top: 0;
    width: 120px;
    padding: 14px 0 0 8px;
    color: var(--ink-black);
    font-size: 15px;
    line-height: 1.15;
    display: flex;
    align-items: flex-start;
    gap: 6px;
  }
  .brand-mark__dot {
    flex: none;
    width: 12px;
    height: 12px;
    margin-top: 3px;
    border-radius: 50%;
    background: var(--ink-black);
  }

  .card__title {
    position: absolute;
    right: 18px;
    top: 70px;
    font-weight: 400;
    font-size: 42px;
    line-height: 1;
    color: var(--ink-white);
    text-shadow: 1px 2px 0 var(--title-shadow);
    white-space: nowrap;
  }

  .mission {
    position: absolute;
    right: 18px;
    top: 196px;
    text-align: right;
    font-size: 26px;
    line-height: 35px;
    color: var(--ink-white);
    white-space: nowrap;
  }

  .verse {
    position: absolute;
    right: 18px;
    top: 186px;
    text-align: right;
    color: var(--ink-white);
    font-size: 26px;
    line-height: 35px;
    white-space: nowrap;
  }
  .verse__ref {
    display: block;
    font-style: normal;
    font-size: 17px;
    line-height: 22px;
    font-weight: 700;
  }

  .contact {
    position: absolute;
    left: 0;
    right: 0;
    top: 362px;
    text-align: center;
    font-style: normal;
    font-size: 16.5px;
    line-height: 21px;
    color: var(--ink-black);
    white-space: nowrap;
  }
</style>
</head>
<body>

  <section class="card card--front" aria-label="Business card front">
    <div class="brand-mark">
      <span class="brand-mark__dot"></span>
      <span>Alder Ridge Helping Harbor</span>
    </div>
    <h1 class="card__title">Alder Ridge Helping Harbor</h1>
    <p class="mission">
      Christ-centered organization dedicated to providing<br>
      compassion and hope to homeless or near homes, families<br>
      and individual by meeting their basic and urgent need of<br>
      food, clothing and shelter.
    </p>
    <address class="contact">
      P.O. Box 287 Brookvale, Pa 18990 Phone: (570) 413-CARE(2273) Toll Free: (855) 413-CARE<br>
      email:Info@alderridgehh.org email:Careline@alderridgehh.org
    </address>
  </section>

  <section class="card card--back" aria-label="Business card back">
    <div class="brand-mark">
      <span class="brand-mark__dot"></span>
      <span>Alder Ridge Helping Harbor</span>
    </div>
    <h2 class="card__title">Alder Ridge Helping Harbor</h2>
    <blockquote class="verse">
      'I was hungry and you gave me something to eat;<br>
      "I was thirsty and you gave me something to drink;<br>
      "I was a stranger and you invited me in."
      <cite class="verse__ref">Matthew 25:35</cite>
    </blockquote>
    <address class="contact">
      P.O. Box 287 Brookvale, Pa 18990 Phone: (570) 413-CARE(2273) Toll Free: (855) 413-CARE<br>
      email:Info@alderridgehh.org email:Careline@alderridgehh.org
    </address>
  </section>

</body>
</html>
```